Austrian finance und insurance broker needs business card design

We Need a serious looking Design for Business Card. we consult private and corporates customers in finance and insurance questions. the final design should express security and experience. We consult customers in questions of loans, Investments and insurance and have a wide range of Banks to offer. We compare several offers and select the best for our customers.

Target Market(s)

private and coporate customers with efforts in Money and insurance

Industry/Entity Type

Insurance Broker

Contact Information for Business Card

Bernhard Aigner
Geschäftsführer
staatl. geprüfter Vermögensberater und Versicherungsmakler
Tel: 0664 521 8409
office@der-brandl.at
www.der-brandl.at
Leopold Hainz Gasse 14
2183 Melkstetten
GISA Nr. 48270315 u. 51736048 (backside)

Font styles to use
Serif
Sans Serif

Requirements
Must have
• logo (designcrowd zip) and all Details
Nice to have
• makler logo design, maybe a 2 coloured Version is possible

```html
<!DOCTYPE html>
<html lang="de">
<head>
<meta charset="utf-8">
<title>Aigner Vermögensberatung – Visitenkarte</title>
<link rel="stylesheet" href="https://fonts.googleapis.com/css2?family=Open+Sans:wght@400;600;700&display=swap">
<style>
  :root {
    --stage: #3a3431;
    --card: #1b1c1e;
    --card-edge: #101112;
    --blue: #2a5fd0;
    --white: #f2f2f2;
    --silver: #8d8f93;
    --text: #e4e4e4;
  }
  * { box-sizing: border-box; margin: 0; padding: 0; }
  html, body { width: 1200px; height: 864px; overflow: hidden; }
  body {
    background: var(--stage);
    font-family: "Open Sans", Arial, sans-serif;
    display: flex;
    align-items: center;
    justify-content: center;
    gap: 40px;
  }
  .card {
    width: 540px;
    height: 350px;
    background: var(--card);
    border: 1px solid var(--card-edge);
    border-radius: 4px;
    box-shadow: 0 14px 30px rgba(0,0,0,.45);
    position: relative;
  }
  .brand { display: flex; align-items: center; gap: 14px; }
  .brand-mark {
    width: 46px; height: 46px; border-radius: 50%;
    border: 3px solid var(--blue); flex: none;
  }
  .brand-name { font-size: 19px; font-weight: 600; color: var(--white); line-height: 1.2; }
  .brand-tagline { font-size: 12.5px; font-weight: 600; color: var(--white); margin-top: 3px; }

  /* back side */
  .card-back { display: flex; flex-direction: column; align-items: center; justify-content: center; gap: 44px; }
  .card-back .brand-mark { border-color: var(--silver); }
  .card-back .brand-name, .card-back .brand-tagline { color: var(--silver); }
  .registry { font-size: 14px; font-weight: 700; color: var(--silver); letter-spacing: .3px; }

  /* front side */
  .card-front .brand { position: absolute; left: 34px; top: 112px; }
  .card-front .brand-name { font-size: 16px; }
  .card-front .brand-tagline { font-size: 11px; }
  .contact-block { position: absolute; right: 30px; top: 150px; width: 230px; }
  .person-name { font-size: 20px; font-weight: 700; color: var(--blue); letter-spacing: .8px; text-transform: uppercase; }
  .person-role { font-size: 15px; font-weight: 700; color: var(--white); text-transform: uppercase; }
  .person-qualification { font-size: 11.5px; font-weight: 600; color: var(--text); line-height: 1.3; margin-top: 6px; }
  .address { font-size: 13px; color: var(--text); line-height: 1.35; margin-top: 10px; }
  .channels { list-style: none; margin-top: 8px; }
  .channels li { display: flex; align-items: center; gap: 8px; font-size: 13px; color: var(--text); line-height: 1.4; }
  .channels svg { width: 11px; height: 11px; fill: var(--blue); flex: none; }
</style>
</head>
<body>

<section class="card card-back">
  <div class="brand">
    <span class="brand-mark"></span>
    <div>
      <div class="brand-name">Aigner Vermögensberatung GmbH</div>
      <div class="brand-tagline">Finanzieren, Versichern, Vorsorgen</div>
    </div>
  </div>
  <p class="registry">GISA Nr. 48270315 u. 51736048</p>
</section>

<section class="card card-front">
  <div class="brand">
    <span class="brand-mark"></span>
    <div>
      <div class="brand-name">Aigner Vermögensberatung GmbH</div>
      <div class="brand-tagline">Finanzieren, Versichern, Vorsorgen</div>
    </div>
  </div>

  <div class="contact-block">
    <h1 class="person-name">Bernhard Aigner</h1>
    <p class="person-role">Geschäftsführer</p>
    <p class="person-qualification">Geprüfter Vermögensberater<br>und Versicherungsmakler</p>
    <p class="address">Leopold Hainz Gasse 14<br>2183 Melkstetten</p>
    <ul class="channels">
      <li><svg viewBox="0 0 12 12"><path d="M2.5 1l2 2.4-1.1 1.3a7 7 0 0 0 3.9 3.9L8.6 7.5 11 9.5 9.8 11C5 11 1 7 1 2.2z"/></svg>0664 521 8409</li>
      <li><svg viewBox="0 0 12 12"><path d="M0 2h12v1.2L6 7 0 3.2zM0 4.6l6 3.8 6-3.8V10H0z"/></svg>office@der-brandl.at</li>
      <li><svg viewBox="0 0 12 12"><path d="M6 0a4 4 0 0 1 4 4c0 3-4 8-4 8S2 7 2 4a4 4 0 0 1 4-4zm0 2.5a1.5 1.5 0 1 0 0 3 1.5 1.5 0 0 0 0-3z"/></svg>www.der-brandl.at</li>
    </ul>
  </div>
</section>

</body>
</html>
```